Website for a Pittsburgh Musical Production

We are creating a website for a musical stage production. Content and copy is included below. We are targeting production in early 2023.

Coded - Design and coding required

1 page

```html
<!DOCTYPE html>
<html lang="en">
<head>
<meta charset="utf-8">
<title>Galvan The Rock Opera</title>
<link rel="stylesheet" href="https://fonts.googleapis.com/css2?family=Rubik:wght@300;400;500;700&family=Lato:ital,wght@0,400;0,700;1,400&display=swap">
<style>
:root{
  --bg:#0f1010;
  --bg-soft:#171a19;
  --bg-footer:#0a0b0b;
  --green:#7c9f50;
  --green-dark:#4d6a33;
  --white:#ffffff;
  --text:#d9d9d9;
  --muted:#9a9a9a;
  --line:#6a6a6a;
}
*{margin:0;padding:0;box-sizing:border-box}
html,body{width:1200px;height:4261px;overflow:hidden;background:var(--bg)}
body{position:relative;font-family:'Lato',sans-serif;color:var(--white)}
.abs{position:absolute}
.heading{font-family:'Rubik',sans-serif;font-weight:700;text-transform:uppercase;text-align:center;width:1200px;left:0;font-size:31px;letter-spacing:.5px}
.rule{position:absolute;left:556px;width:88px;height:5px;border-top:1px solid var(--green);border-bottom:1px solid var(--green)}
/* header */
.site-header{position:absolute;left:0;top:0;width:1200px;height:105px;background:rgba(8,9,9,.85);z-index:3}
.brand{position:absolute;left:152px;top:18px;font-family:'Rubik',sans-serif;font-weight:500;font-size:26px;color:var(--green);line-height:1.1}
.brand small{display:block;font-size:13px;color:var(--white);margin-left:110px}
.socials{position:absolute;left:592px;top:17px;display:flex;gap:5px}
.socials span{width:30px;height:30px;border:2px solid var(--white);border-radius:50%}
.call{position:absolute;left:780px;top:16px;display:flex;align-items:center;gap:10px;font-family:'Rubik',sans-serif;font-weight:500;font-size:17px}
.call .ring{width:32px;height:32px;border:2px solid var(--white);border-radius:50%;display:flex;align-items:center;justify-content:center}
.nav{position:absolute;left:408px;top:68px;display:flex;gap:23px;font-family:'Rubik',sans-serif;font-weight:500;font-size:13.5px;text-transform:uppercase}
.nav .active{color:var(--green)}
/* hero */
.hero{position:absolute;left:0;top:0;width:1200px;height:775px;background:radial-gradient(ellipse at 55% 40%,#24291f 0%,#141713 55%,#0f1010 100%)}
.hero-art{position:absolute;left:150px;top:115px;width:280px;height:630px;background:radial-gradient(ellipse at 50% 45%,#4d6637 0%,#2a3720 50%,rgba(20,24,18,0) 75%)}
.hero-title{position:absolute;left:500px;top:205px;width:520px;text-align:center;font-family:'Rubik',sans-serif;font-weight:500;font-size:66px;color:var(--green);line-height:1}
.hero-title small{display:block;font-size:23px;color:var(--white);font-weight:400;margin:8px 0 0 110px}
.hero-lines{position:absolute;left:460px;top:392px;width:600px;text-align:center;font-family:'Rubik',sans-serif;font-size:37px;line-height:48px;font-weight:300}
.hero-lines b{display:block;color:var(--green);font-weight:700}
.btn{position:absolute;display:flex;align-items:center;justify-content:center;gap:12px;border-radius:26px;font-family:'Rubik',sans-serif;font-weight:700;font-size:16px;text-transform:uppercase}
.btn-outline{border:2px solid var(--white)}
.btn-green{background:var(--green)}
.arrow{position:absolute;width:34px;height:34px;border-radius:50%;background:rgba(0,0,0,.45);display:flex;align-items:center;justify-content:center}
/* shows */
.show-card{position:absolute;width:440px;height:231px;border:2px solid var(--line);background:#121313}
.show-photo{position:absolute;left:6px;top:8px;width:166px;height:212px}
.show-date{position:absolute;left:195px;top:28px;width:38px;height:36px;background:var(--green);font-family:'Rubik',sans-serif;font-size:9px;text-align:center;line-height:11px;padding-top:7px}
.show-title{position:absolute;left:247px;top:22px;font-family:'Rubik',sans-serif;font-weight:700;font-size:16.5px;line-height:21px;text-transform:uppercase}
.show-venue{position:absolute;left:195px;top:82px;font-style:italic;font-size:13.5px;display:flex;align-items:center;gap:9px}
.show-text{position:absolute;left:195px;top:110px;width:230px;font-size:13.5px;line-height:18px;color:var(--text)}
.show-btn{position:absolute;left:195px;top:166px;width:138px;height:34px;border-radius:17px;background:var(--green);font-family:'Rubik',sans-serif;font-weight:700;font-size:13px;display:flex;align-items:center;justify-content:center}
.big-arrow{position:absolute;top:1172px}
/* welcome */
.welcome{position:absolute;left:0;top:1530px;width:1200px;height:600px;background:linear-gradient(180deg,#111312 0%,#1b1f1c 45%,#111312 100%)}
.welcome-to{position:absolute;top:1655px;width:1200px;text-align:center;font-family:'Rubik',sans-serif;font-weight:300;font-size:35px}
.welcome-title{position:absolute;top:1705px;width:1200px;text-align:center;font-family:'Rubik',sans-serif;font-weight:700;font-size:35px}
.body-copy{position:absolute;text-align:center;color:var(--text);font-size:16.5px;line-height:25px}
/* gallery */
.tile{position:absolute}
/* testimonial */
.testimonial{position:absolute;left:0;top:2995px;width:1200px;height:440px;background:linear-gradient(180deg,#151817,#1c201d 60%,#141615)}
.quote{position:absolute;left:240px;top:3178px;width:720px;text-align:center;font-size:17px;line-height:25px;color:var(--text)}
.quote-mark{font-family:'Rubik',sans-serif;font-weight:700;font-size:44px;line-height:0;vertical-align:-14px}
/* newsletter */
.field{position:absolute;top:3692px;height:52px;background:var(--white);color:#777;font-size:14px;padding:0 26px;display:flex;align-items:center}
.subscribe{position:absolute;left:853px;top:3692px;width:160px;height:52px;background:var(--green);font-family:'Rubik',sans-serif;font-weight:700;font-size:15px;display:flex;align-items:center;justify-content:center}
/* footer */
.site-footer{position:absolute;left:0;top:3910px;width:1200px;height:351px;background:var(--bg-footer)}
.contact-icon{position:absolute;width:44px;height:44px;border:2px solid var(--white);border-radius:50%;display:flex;align-items:center;justify-content:center}
.contact-label{position:absolute;font-family:'Rubik',sans-serif;font-weight:500;font-size:15px}
.contact-value{position:absolute;font-size:15px;color:var(--text)}
.foot-social{position:absolute;width:38px;height:38px;border:2px solid var(--green);border-radius:50%}
</style>
</head>
<body>

<section class="hero">
  <div class="hero-art" role="img" aria-label="Sketched green illustration of the show's lead character"></div>
  <div class="hero-title">Galvan<small>the rock opera</small></div>
  <div class="hero-lines">NEMO ENIM IPSAM PORRO<b>VOLUPTATEM QUIA ENIM</b>VOLUPTAS SIT</div>
  <a class="btn btn-outline" style="left:559px;top:572px;width:184px;height:50px">Find Tickets</a>
  <a class="btn btn-green" style="left:761px;top:572px;width:196px;height:50px">Watch Video
    <svg width="28" height="28" viewBox="0 0 28 28"><circle cx="14" cy="14" r="12" fill="none" stroke="#fff" stroke-width="2.5"/><path d="M11 8.5l8 5.5-8 5.5z" fill="#fff"/></svg></a>
  <div class="arrow" style="left:74px;top:401px"><svg width="12" height="14" viewBox="0 0 12 14"><path d="M8 1L2 7l6 6" fill="none" stroke="#fff" stroke-width="1.6"/></svg></div>
  <div class="arrow" style="left:1090px;top:401px"><svg width="12" height="14" viewBox="0 0 12 14"><path d="M4 1l6 6-6 6" fill="none" stroke="#fff" stroke-width="1.6"/></svg></div>
</section>

<header class="site-header">
  <div class="brand">Galvan<small>the rock opera</small></div>
  <div class="socials"><span></span><span></span><span></span><span></span><span></span></div>
  <div class="call"><span class="ring"><svg width="16" height="16" viewBox="0 0 24 24"><path d="M6.6 10.8a15 15 0 006.6 6.6l2.2-2.2c.3-.3.7-.4 1-.2 1.1.4 2.3.6 3.6.6.6 0 1 .4 1 1V20c0 .6-.4 1-1 1A17 17 0 013 4c0-.6.4-1 1-1h3.5c.6 0 1 .4 1 1 0 1.3.2 2.5.6 3.6.1.3 0 .7-.2 1z" fill="#fff"/></svg></span>Call Us : (555) 0142 3300</div>
  <nav class="nav"><span class="active">Home</span><span>Upcoming Shows</span><span>Past Shows</span><span>Gallery</span><span>Reviews</span><span>About</span><span>Contact</span></nav>
</header>

<h2 class="heading abs" style="top:843px">Upcoming Shows</h2>
<div class="rule" style="top:900px"></div>

<div class="abs big-arrow" style="left:80px"><svg width="22" height="36" viewBox="0 0 22 36"><path d="M18 3L4 18l14 15" fill="none" stroke="#fff" stroke-width="3"/></svg></div>
<div class="abs big-arrow" style="left:1098px"><svg width="22" height="36" viewBox="0 0 22 36"><path d="M4 3l14 15L4 33" fill="none" stroke="#fff" stroke-width="3"/></svg></div>

<article class="show-card" style="left:143px;top:957px">
  <div class="show-photo" role="img" aria-label="Concert crowd under blue stage lights" style="background:linear-gradient(180deg,#3a4fb0,#5a3a70 45%,#2a160c)"></div>
  <div class="show-date">JUN<br>25</div>
  <div class="show-title">Nulla at diam<br>ornare, aliquam</div>
  <div class="show-venue"><svg width="13" height="13" viewBox="0 0 14 14"><circle cx="7" cy="7" r="5.5" fill="none" stroke="#7c9f50" stroke-width="1.5"/><path d="M7 4v3.3h2.4" fill="none" stroke="#7c9f50" stroke-width="1.5"/></svg>Arena Vesperi 9:30 PM</div>
  <p class="show-text">Sed ut perspiciatis unde omnis iste natus sit voluptatem</p>
  <a class="show-btn">FIND TICKETS</a>
</article>
<article class="show-card" style="left:616px;top:957px">
  <div class="show-photo" role="img" aria-label="Fireworks over a concert audience" style="background:linear-gradient(180deg,#2a1410,#6a2a22 40%,#1c0f0c)"></div>
  <div class="show-date">JUN<br>25</div>
  <div class="show-title">Nulla at diam<br>ornare, aliquam</div>
  <div class="show-venue"><svg width="13" height="13" viewBox="0 0 14 14"><circle cx="7" cy="7" r="5.5" fill="none" stroke="#7c9f50" stroke-width="1.5"/><path d="M7 4v3.3h2.4" fill="none" stroke="#7c9f50" stroke-width="1.5"/></svg>Arena Vesperi 9:30 PM</div>
  <p class="show-text">Sed ut perspiciatis unde omnis iste natus sit voluptatem</p>
  <a class="show-btn">FIND TICKETS</a>
</article>
<article class="show-card" style="left:143px;top:1212px">
  <div class="show-photo" role="img" aria-label="Empty stage with a microphone stand" style="background:linear-gradient(180deg,#5a3a28,#2e1e16 60%,#150e0a)"></div>
  <div class="show-date">JUN<br>25</div>
  <div class="show-title">Nulla at diam<br>ornare, aliquam</div>
  <div class="show-venue"><svg width="13" height="13" viewBox="0 0 14 14"><circle cx="7" cy="7" r="5.5" fill="none" stroke="#7c9f50" stroke-width="1.5"/><path d="M7 4v3.3h2.4" fill="none" stroke="#7c9f50" stroke-width="1.5"/></svg>Arena Vesperi 9:30 PM</div>
  <p class="show-text">Sed ut perspiciatis unde omnis iste natus sit voluptatem</p>
  <a class="show-btn">FIND TICKETS</a>
</article>
<article class="show-card" style="left:616px;top:1212px">
  <div class="show-photo" role="img" aria-label="Retro live rock night poster" style="background:linear-gradient(180deg,#efe6cf,#e9d9b8 70%,#d9583a)"></div>
  <div class="show-date">JUN<br>25</div>
  <div class="show-title">Nulla at diam<br>ornare, aliquam</div>
  <div class="show-venue"><svg width="13" height="13" viewBox="0 0 14 14"><circle cx="7" cy="7" r="5.5" fill="none" stroke="#7c9f50" stroke-width="1.5"/><path d="M7 4v3.3h2.4" fill="none" stroke="#7c9f50" stroke-width="1.5"/></svg>Arena Vesperi 9:30 PM</div>
  <p class="show-text">Sed ut perspiciatis unde omnis iste natus sit voluptatem</p>
  <a class="show-btn">FIND TICKETS</a>
</article>

<section class="welcome" role="img" aria-label="Dim photo of a concert crowd with raised hands"></section>
<svg class="abs" style="left:0;top:1570px" width="1200" height="70" viewBox="0 0 1200 70"><path d="M680 15L1200 0v70z" fill="#7c9f50"/></svg>
<div class="welcome-to">Welcome to</div>
<div class="welcome-title">Galvan The Rock Opera</div>
<div class="rule" style="top:1770px"></div>
<p class="body-copy" style="left:185px;top:1803px;width:830px">Sed ut perspiciatis unde omnis iste natus error sit voluptatem accusantium doloremque laudantium, totam rem aperiam, eaque ipsa quae ab illo inventore veritatis et quasi architecto beatae vitae dicta sunt explicabo. Nemo enim ipsam voluptatem quia voluptas sit aspernatur aut odit aut fugit, sed quia consequuntur magni dolores eos qui ratione voluptatem sequi nesciunt. Neque porro quisquam est, qui dolorem ipsum quia dolor sit amet, consectetur, adipisci velit, sed quia non numquam eius modi tempora incidunt ut labore et dolore magnam aliquam quaerat voluptatem. Ut enim ad minima veniam</p>
<a class="btn btn-outline" style="left:517px;top:1984px;width:166px;height:46px;font-weight:500;font-size:15px">Learn More</a>

<h2 class="heading abs" style="top:2207px">Gallery</h2>
<div class="rule" style="top:2263px"></div>
<div class="tile" role="img" aria-label="Show artwork with the green sketched character" style="left:144px;top:2307px;width:304px;height:283px;background:radial-gradient(ellipse at 30% 50%,#3c4e2c,#0b0c0b 70%)"></div>
<div class="tile" role="img" aria-label="Night artwork of a lone figure on a peak under a bright moon" style="left:458px;top:2307px;width:282px;height:283px;background:linear-gradient(180deg,#8a897c 0%,#4a4a46 45%,#1a1c20 80%,#111214 100%)"></div>
<div class="tile" role="img" aria-label="Hands forming a heart at a concert" style="left:751px;top:2307px;width:305px;height:283px;background:radial-gradient(ellipse at 50% 35%,#7fd4b0,#2a7a5a 45%,#0e2a20)"></div>
<div class="tile" role="img" aria-label="Collage of band promo photos" style="left:144px;top:2600px;width:304px;height:284px;background:linear-gradient(135deg,#5a2a3a,#2a1a20 50%,#c8b8a8)"></div>
<div class="tile" role="img" aria-label="Painted album cover in warm colours" style="left:458px;top:2600px;width:282px;height:284px;background:linear-gradient(135deg,#3a3ab0,#c85a4a 50%,#e8c060)"></div>
<div class="tile" role="img" aria-label="Dark fantasy album cover with a woman in red" style="left:751px;top:2600px;width:305px;height:284px;background:radial-gradient(ellipse at 55% 70%,#c0502a,#5a1a10 45%,#1a0c08)"></div>

<section class="testimonial" role="img" aria-label="Faint dark texture background"></section>
<h2 class="abs" style="top:3068px;width:1200px;text-align:center;font-family:'Rubik',sans-serif;font-weight:700;font-size:37px">Client Testimonial</h2>
<div class="rule" style="top:3140px"></div>
<div class="abs" style="left:143px;top:3209px"><svg width="14" height="24" viewBox="0 0 14 24"><path d="M12 2L2 12l10 10" fill="none" stroke="#fff" stroke-width="2.5"/></svg></div>
<div class="abs" style="left:1040px;top:3209px"><svg width="14" height="24" viewBox="0 0 14 24"><path d="M2 2l10 10L2 22" fill="none" stroke="#fff" stroke-width="2.5"/></svg></div>
<p class="quote"><span class="quote-mark">&ldquo;</span> Sed ut perspiciatis unde omnis iste natus error sit voluptatem accusantium doloremque laudantium, totam rem aperiam, eaque ipsa quae ab illo inventore veritatis et quasi architecto beatae vitae dicta sunt explicabo. Nemo enim ipsam voluptatem quia voluptas sit aspernatur aut odit aut fugit Sed ut perspiciatis undevoluptatem</p>
<p class="abs" style="left:530px;top:3300px;font-size:17px;color:var(--text)">&mdash; Blandit Lectus <span class="quote-mark" style="color:#fff;margin-left:14px">&rdquo;</span></p>
<svg class="abs" style="left:0;top:3365px" width="1200" height="70" viewBox="0 0 1200 70"><path d="M0 0L520 70H0z" fill="#7c9f50"/></svg>

<h2 class="heading abs" style="top:3530px;font-size:29px">Join Our Newsletter</h2>
<div class="rule" style="top:3582px"></div>
<p class="body-copy" style="left:230px;top:3615px;width:740px;font-size:15.5px;line-height:22px">Sed ut perspiciatis unde omnis iste natus error sit voluptatem accusantium doloremque laudantium, totam rem aperiam, eaque ipsa quae ab illo inventore veritatis et quasi architecto</p>
<div class="field" style="left:186px;width:303px">Name</div>
<div class="field" style="left:508px;width:327px">Email Address*</div>
<a class="subscribe">SUBSCRIBE</a>

<footer class="site-footer">
  <div class="abs" role="img" aria-label="Green sketched character artwork" style="left:160px;top:40px;width:120px;height:240px;background:radial-gradient(ellipse at 50% 45%,#4d6637,#22301a 50%,rgba(10,11,11,0) 75%)"></div>
  <div class="abs" style="left:280px;top:115px;font-family:'Rubik',sans-serif;font-weight:500;font-size:24px;color:var(--green);line-height:1.1">Galvan<small style="display:block;font-size:11px;color:#fff;margin-left:88px">the rock opera</small></div>

  <div class="contact-icon" style="left:477px;top:57px"><svg width="18" height="22" viewBox="0 0 18 22"><path d="M9 1a7 7 0 00-7 7c0 5 7 13 7 13s7-8 7-13a7 7 0 00-7-7z" fill="#fff"/><circle cx="9" cy="8" r="2.6" fill="#0a0b0b"/></svg></div>
  <div class="contact-label" style="left:545px;top:52px">Address:</div>
  <div class="contact-value" style="left:545px;top:74px">1028 enim ipsam voluptatem</div>

  <div class="contact-icon" style="left:841px;top:57px"><svg width="20" height="20" viewBox="0 0 24 24"><path d="M6.6 10.8a15 15 0 006.6 6.6l2.2-2.2c.3-.3.7-.4 1-.2 1.1.4 2.3.6 3.6.6.6 0 1 .4 1 1V20c0 .6-.4 1-1 1A17 17 0 013 4c0-.6.4-1 1-1h3.5c.6 0 1 .4 1 1 0 1.3.2 2.5.6 3.6.1.3 0 .7-.2 1z" fill="#fff"/></svg></div>
  <div class="contact-label" style="left:908px;top:52px">Phone:</div>
  <div class="contact-value" style="left:908px;top:72px;font-family:'Rubik',sans-serif;font-weight:500;font-size:18px;color:#fff">(555) 0188 6600</div>

  <div class="contact-icon" style="left:477px;top:158px"><svg width="20" height="16" viewBox="0 0 20 16"><rect x="1" y="1" width="18" height="14" rx="2" fill="#fff"/><path d="M2 3l8 6 8-6" fill="none" stroke="#0a0b0b" stroke-width="1.6"/></svg></div>
  <div class="contact-label" style="left:538px;top:152px">Email:</div>
  <div class="contact-value" style="left:538px;top:175px">info@galvanrockopera.com</div>

  <div class="foot-social" style="left:843px;top:158px"></div>
  <div class="foot-social" style="left:891px;top:158px"></div>
  <div class="foot-social" style="left:939px;top:158px"></div>

  <div class="abs" style="left:478px;top:217px;width:577px;height:1px;background:#2e302f"></div>
  <p class="abs" style="right:145px;top:262px;font-size:15px;color:var(--text)">Galvan The Rock Opera &copy; 2021 All Rights Reserved &nbsp;|&nbsp; Privacy policy &nbsp;|&nbsp; Terms of service</p>
</footer>

</body>
</html>
```